Executive Headhunting and Recruitment Business

Looking for a website for an executive recruitment and headhunting business based in the UK. We provide headhunting services to the recruitment sector.

I'm pretty open to ideas as long as the website stands out but in a professional way. We are not a budget business, the service we provide is definitely not the cheapest but we are the best at what we do, our value is in our service and we are a high-end business aiming at companies who want to pay for the service they receive so our website should reflect this.

Website should be professional and clean looking.
Updates

Logo now added to Files. Added Saturday, February 13, 2016

Target Market(s)

Recruitment Agencies

Industry/Entity Type

Business

Coding

Coded - Design and coding required

Number of Pages Required

4 page

Requirements
Must have
• Home Page - Current Vacancies - About us - Contact Us
• Clean - Modern - Professional
Nice to have
• Open to ideas.

```html
<!DOCTYPE html>
<html lang="en">
<head>
<meta charset="utf-8">
<title>Hartwell Ashby – Executive Recruitment</title>
<link href="https://fonts.googleapis.com/css2?family=Cinzel:wght@400;700&family=Raleway:wght@500;600&family=Open+Sans:wght@400;600;700&display=swap" rel="stylesheet">
<style>
:root{
  --blue:#0a56a8;
  --blue-dark:#084a92;
  --partner:#1d4f86;
  --ink:#2b2b2b;
  --muted:#8a8a8a;
  --band:#eeeeee;
  --white:#ffffff;
}
*{margin:0;padding:0;box-sizing:border-box}
html,body{width:720px;height:1200px;overflow:hidden;background:var(--white)}
body{position:relative;font-family:"Open Sans",Arial,sans-serif;color:var(--ink)}
.abs{position:absolute}

/* header */
.site-header{position:absolute;left:0;top:0;width:720px;height:62px;background:var(--white)}
.brand{position:absolute;left:60px;top:20px;display:flex;align-items:center;gap:8px}
.brand-mark{width:14px;height:14px;background:var(--blue)}
.brand-name{font-family:"Cinzel",serif;font-size:15px;font-weight:400;color:var(--blue);letter-spacing:1px}
.main-nav{position:absolute;left:278px;top:0;height:62px;display:flex}
.main-nav a{font-family:"Cinzel",serif;font-size:8.5px;color:var(--ink);text-decoration:none;height:62px;line-height:72px;padding:0 13px;letter-spacing:.3px}
.main-nav a.active{background:var(--blue);color:var(--white);font-weight:700;padding:0 6px;width:41px;text-align:center}

/* hero */
.hero{position:absolute;left:0;top:62px;width:720px;height:407px;
  background:linear-gradient(180deg,#c7d3db 0%,#9fb0bc 35%,#3c4650 62%,#7d8c97 78%,#a9b7c0 100%)}
.hero-arrow{position:absolute;top:248px}
.hero-title{position:absolute;left:0;top:328px;width:720px;text-align:center;font-family:"Cinzel",serif;font-weight:400;font-size:27px;color:var(--white);letter-spacing:1px;text-shadow:0 1px 3px rgba(0,0,0,.5)}
.hero-sub{position:absolute;left:0;top:364px;width:720px;text-align:center;font-family:Arial,sans-serif;font-size:15px;color:var(--white);letter-spacing:.5px}
.job-search{position:absolute;left:118px;top:396px;width:489px;height:35px;background:var(--white);border:1px solid #fff}
.job-search span{position:absolute;left:10px;top:10px;font-size:8.5px;font-style:italic;color:#888}
.job-search button{position:absolute;right:1px;top:1px;width:106px;height:31px;border:0;background:var(--blue);color:var(--white);font:700 12px Arial,sans-serif;display:flex;align-items:center;justify-content:center;gap:6px}

.bump{position:absolute;width:74px;height:37px;background:var(--white);border-radius:37px 37px 0 0}

/* about */
.section-title{position:absolute;left:0;width:720px;text-align:center;font-family:"Cinzel",serif;font-weight:400;font-size:18px;color:var(--ink);letter-spacing:1px}
.title-rule{position:absolute;left:337px;width:47px;height:2px;background:var(--blue)}
.about-text{position:absolute;left:70px;top:548px;width:580px;text-align:center;font-size:7.6px;line-height:13.5px;color:var(--muted)}

.service-card{position:absolute;top:658px;width:188px;height:184px;text-align:center}
.service-card.highlight{background:linear-gradient(180deg,#f3f3f3 0%,#ffffff 100%);border-bottom:2px solid var(--blue)}
.service-icon{position:absolute;width:94px;height:94px;border-radius:50%;background:var(--blue);display:flex;align-items:center;justify-content:center}
.service-card h3{position:absolute;left:0;top:86px;width:188px;font-family:"Cinzel",serif;font-weight:400;font-size:13px;letter-spacing:.8px}
.service-card p{position:absolute;left:8px;top:112px;width:172px;font-size:7.4px;line-height:12px;color:var(--muted)}
.read-more{position:absolute;left:0;top:158px;width:188px;font-size:8px;font-weight:700;color:var(--blue);display:flex;justify-content:center;align-items:center;gap:4px}

/* partners */
.partners{position:absolute;left:0;top:917px;width:720px;height:131px;background:var(--band)}
.partner{position:absolute;top:994px;height:24px;font-family:"Open Sans",sans-serif;font-size:14px;font-weight:600;color:var(--partner);display:flex;align-items:center;justify-content:center;gap:6px;white-space:nowrap}
.partner i{display:block;width:18px;height:18px;border-radius:50%;background:var(--partner)}
.carousel-btn{position:absolute;top:992px;width:27px;height:27px;border-radius:50%;background:#c9c9c9}

/* footer */
.site-footer{position:absolute;left:0;top:1048px;width:720px;height:152px;background:var(--blue);color:var(--white)}
.footer-col{position:absolute;top:22px}
.footer-col h4{font-family:"Raleway",sans-serif;font-weight:600;font-size:11.5px}
.footer-col .rule{height:1px;background:rgba(255,255,255,.45);margin-top:6px}
.footer-col .rule::before{content:"";display:block;width:32px;height:2px;background:#cfe0f3}
.footer-small{font-size:7.2px;line-height:13px}
.footer-list{list-style:none;margin-top:9px}
.footer-list li{font-size:7.2px;line-height:13px;padding-left:11px;position:relative}
.footer-list li::before{content:"";position:absolute;left:2px;top:4px;border-left:3px solid #fff;border-top:2.5px solid transparent;border-bottom:2.5px solid transparent}
.phone{font-size:10px;font-weight:700;margin-top:8px;display:flex;align-items:center;gap:6px}
.newsletter{display:flex;margin-top:13px;gap:6px}
.newsletter .field{width:106px;height:20px;background:var(--blue-dark);border:1px solid #0d4380;font-size:7.5px;padding:5px 6px}
.newsletter .btn{width:48px;height:20px;background:#d6d6d6;color:#333;font-size:8px;text-align:center;line-height:20px}
.social{display:flex;gap:7px;margin-top:13px}
.social span{width:19px;height:19px;border-radius:50%;border:1.5px solid var(--white)}
.footer-divider{position:absolute;left:58px;top:124px;width:603px;height:1px;background:rgba(255,255,255,.25)}
.copyright{position:absolute;left:0;top:132px;width:720px;text-align:center;font-size:7px}
</style>
</head>
<body>

<header class="site-header">
  <div class="brand"><span class="brand-mark"></span><span class="brand-name">HARTWELL ASHBY</span></div>
  <nav class="main-nav">
    <a class="active" href="#">HOME</a>
    <a href="#">ABOUT US</a>
    <a href="#">SERVICES</a>
    <a href="#">FOR EMPLOYERS</a>
    <a href="#">CONTACT US</a>
  </nav>
</header>

<section class="hero" role="img" aria-label="Silhouetted business people meeting in front of a bright office window"></section>
<svg class="hero-arrow" style="left:36px" width="12" height="36" viewBox="0 0 12 36"><path d="M10 2 L2 18 L10 34" fill="none" stroke="#fff" stroke-width="1.5"/></svg>
<svg class="hero-arrow" style="left:672px" width="12" height="36" viewBox="0 0 12 36"><path d="M2 2 L10 18 L2 34" fill="none" stroke="#fff" stroke-width="1.5"/></svg>
<h1 class="hero-title">WELCOME TO HARTWELL ASHBY</h1>
<p class="hero-sub">RECRUIT ● REWARD ● CANDIDATES</p>
<div class="job-search">
  <span>Find the right Job..</span>
  <button><svg width="16" height="16" viewBox="0 0 16 16"><circle cx="6.5" cy="6.5" r="5" fill="none" stroke="#fff" stroke-width="2"/><path d="M10 10 L15 15" stroke="#fff" stroke-width="2.4"/></svg>Search here</button>
</div>
<div class="bump" style="left:323px;top:432px"></div>

<h2 class="section-title" style="top:512px">HARTWELL ABOUT US</h2>
<div class="title-rule" style="top:539px"></div>
<p class="about-text">Lorem ipsum dolor sit amet, consectetur adipiscing elit, sed do eiusmod tempor incididunt ut l laboris nisi ut aliquip ex ea commodo consequat. Duis aute irure dolor in reprehenderit in voluptate velit esse cillum dolore eu fugiat nulla pariatur. Sed ut perspiciatis unde omnis iste natus error sit voluptatem accusantium doloremque laudantium,&nbsp; dicta sunt explicabo.</p>

<div class="service-card highlight" style="left:60px">
  <h3>CANDIDATE</h3>
  <p>Lorem ipsum dolor sit amet, consectetur adipiscing elit, sed do eiusmod tempor incid-idunt ut labore et dolore magna aliqua.</p>
  <div class="read-more">Read More <svg width="9" height="9" viewBox="0 0 9 9"><circle cx="4.5" cy="4.5" r="4.5" fill="#0a56a8"/><path d="M3.5 2.5 L5.5 4.5 L3.5 6.5" fill="none" stroke="#fff" stroke-width="1.2"/></svg></div>
</div>
<div class="service-card" style="left:268px">
  <h3>CLIENTS</h3>
  <p>Lorem ipsum dolor sit amet, consectetur adipiscing elit, sed do eiusmod tempor incid-idunt ut labore et dolore magna aliqua.</p>
  <div class="read-more">Read More <svg width="9" height="9" viewBox="0 0 9 9"><circle cx="4.5" cy="4.5" r="4.5" fill="#0a56a8"/><path d="M3.5 2.5 L5.5 4.5 L3.5 6.5" fill="none" stroke="#fff" stroke-width="1.2"/></svg></div>
</div>
<div class="service-card" style="left:482px">
  <h3>CONSULTANT</h3>
  <p>Lorem ipsum dolor sit amet, consectetur adipiscing elit, sed do eiusmod tempor incid-idunt ut labore et dolore magna aliqua.</p>
  <div class="read-more">Read More <svg width="9" height="9" viewBox="0 0 9 9"><circle cx="4.5" cy="4.5" r="4.5" fill="#0a56a8"/><path d="M3.5 2.5 L5.5 4.5 L3.5 6.5" fill="none" stroke="#fff" stroke-width="1.2"/></svg></div>
</div>

<div class="service-icon" style="left:107px;top:639px">
  <svg width="56" height="56" viewBox="0 0 56 56"><circle cx="32" cy="24" r="16" fill="none" stroke="#fff" stroke-width="4"/><circle cx="32" cy="20" r="5" fill="#fff"/><path d="M23 34 Q32 24 41 34" fill="#fff"/><path d="M20 36 L6 50" stroke="#fff" stroke-width="5" stroke-linecap="round"/></svg>
</div>
<div class="service-icon" style="left:315px;top:639px">
  <svg width="60" height="46" viewBox="0 0 60 46"><circle cx="16" cy="12" r="7" fill="#fff"/><circle cx="44" cy="12" r="7" fill="#fff"/><path d="M2 34 Q2 22 16 22 Q30 22 30 34Z" fill="#fff"/><path d="M30 34 Q30 22 44 22 Q58 22 58 34Z" fill="#fff"/><circle cx="30" cy="20" r="8" fill="#fff" stroke="#0a56a8" stroke-width="2"/><path d="M14 44 Q14 30 30 30 Q46 30 46 44Z" fill="#fff" stroke="#0a56a8" stroke-width="2"/></svg>
</div>
<div class="service-icon" style="left:529px;top:639px">
  <svg width="46" height="42" viewBox="0 0 46 42"><rect x="15" y="2" width="16" height="8" fill="none" stroke="#fff" stroke-width="3"/><rect x="2" y="9" width="42" height="31" fill="#fff"/><rect x="2" y="15" width="42" height="2" fill="#0a56a8"/></svg>
</div>

<section class="partners"></section>
<div class="bump" style="left:323px;top:880px"></div>
<div class="abs" style="left:323px;top:917px;width:74px;height:20px;background:var(--white);border-radius:0 0 37px 37px"></div>
<h2 class="section-title" style="top:945px;font-size:15px">OUR PARTNERS</h2>
<div class="title-rule" style="top:967px"></div>
<div class="carousel-btn" style="left:19px"><svg width="27" height="27" viewBox="0 0 27 27"><path d="M15 8 L10 13.5 L15 19" fill="none" stroke="#fff" stroke-width="1.6"/></svg></div>
<div class="partner" style="left:50px;width:130px">Corvane</div>
<div class="partner" style="left:205px;width:130px">Meridex</div>
<div class="partner" style="left:357px;width:160px"><i></i>Ashgrove Ventures</div>
<div class="partner" style="left:525px;width:136px">Northfield Energy</div>
<div class="carousel-btn" style="left:673px"><svg width="27" height="27" viewBox="0 0 27 27"><path d="M12 8 L17 13.5 L12 19" fill="none" stroke="#fff" stroke-width="1.6"/></svg></div>

<footer class="site-footer">
  <div class="footer-col" style="left:58px;width:137px">
    <h4>Contact us</h4><div class="rule"></div>
    <div style="display:flex;gap:9px;margin-top:9px">
      <svg width="9" height="12" viewBox="0 0 9 12"><path d="M4.5 12 L0.8 6 A4.2 4.2 0 1 1 8.2 6Z" fill="#fff"/><circle cx="4.5" cy="4.3" r="1.6" fill="#0a56a8"/></svg>
      <div class="footer-small">1200 Sample Street #100<br>Westbrook 40012</div>
    </div>
    <div class="phone"><svg width="12" height="9" viewBox="0 0 12 9"><path d="M0 3 Q6 -1 12 3 L10 4.5 L8 3 L4 3 L2 4.5Z M2 5 L10 5 L11 9 L1 9Z" fill="#fff"/></svg>555-014-2290</div>
  </div>
  <div class="footer-col" style="left:239px;width:49px">
    <h4>Services</h4><div class="rule"></div>
    <ul class="footer-list"><li>Candidate</li><li>Clients</li><li>Consultant</li></ul>
  </div>
  <div class="footer-col" style="left:362px">
    <h4>Newsletter Sign Up</h4><div class="rule" style="width:100px"></div>
    <div class="newsletter"><div class="field">Email Address</div><div class="btn">Sign Up</div></div>
  </div>
  <div class="footer-col" style="left:561px">
    <h4>Social Media</h4><div class="rule" style="width:70px"></div>
    <div class="social"><span></span><span></span><span></span><span></span></div>
  </div>
  <div class="footer-divider"></div>
  <p class="copyright">Copyright © 2014. All Rights Reserved</p>
</footer>

</body>
</html>
```